Dunvarra windows & Home Improvements

We are a family run business with over 35 years expertise. Myself and father run it
We supply and install a rated windows and all types of doors and
Verandel composite doors .
We also specialise in renovating houses and adding extensions on to houses .
Are biggest selling point is the quality of the products we provide . we give 15 year guarantee on all windows and doors

I need flyers to distribute at shows and also to put through letterboxes
they can be a6 or a5 which ever works best . I have attached some images and our logo. Images don't have to be used

I have a show on the 29th march so need them fairly fast. Been designing them myself on this but they just don't look right

```html
<!DOCTYPE html>
<html lang="en">
<head>
<meta charset="utf-8">
<title>Dunvarra Windows &amp; Home Improvements – Flyer</title>
<link href="https://fonts.googleapis.com/css2?family=Oswald:wght@500;600;700&family=Source+Sans+3:wght@400;600&display=swap" rel="stylesheet">
<style>
  :root{
    --brand-blue:#1f63b6;
    --deep-blue:#174f98;
    --ink:#1b1b1d;
    --paper:#f4f4f4;
    --panel-grey:#d6d7d9;
    --stage:#e9e6e1;
    --white:#ffffff;
  }
  *{margin:0;padding:0;box-sizing:border-box}
  html,body{width:1200px;height:1013px;overflow:hidden}
  body{background:var(--stage);position:relative;font-family:"Source Sans 3",Arial,sans-serif;color:var(--ink)}
  .flyer{position:absolute;top:145px;width:560px;height:722px;overflow:hidden;background:var(--paper);box-shadow:0 6px 18px rgba(0,0,0,.18)}
  .flyer--front{left:25px}
  .flyer--back{left:615px}
  .flyer svg.backdrop{position:absolute;left:0;top:0;width:560px;height:722px}
  .abs{position:absolute}
  .headline{font-family:"Oswald",Impact,sans-serif;font-weight:600;text-align:center;left:0;width:560px}
  .headline--dark{top:458px;font-size:25px;color:var(--ink);letter-spacing:.2px}
  .headline--blue{top:490px;font-size:21px;line-height:27px;color:var(--brand-blue)}
  .intro{top:562px;left:30px;width:500px;text-align:center;font-size:18px;line-height:22px}
  .social{font-size:14px;display:flex;align-items:center;gap:5px}
  .social i{display:inline-block;width:12px;height:12px;background:#6b6f78;border-radius:2px}
  .cta{left:0;width:560px;text-align:center;color:var(--white)}
  .cta-label{top:657px;font-size:15px;font-weight:600}
  .cta-phone{top:676px;font-family:"Oswald",Impact,sans-serif;font-weight:700;font-size:25px;letter-spacing:.3px}
  .badge{left:365px;top:310px;width:170px;height:120px;display:flex;flex-direction:column;align-items:center;justify-content:center;text-align:center;font-family:"Oswald",sans-serif;font-weight:600;color:var(--deep-blue);font-size:14px;line-height:16px}
  .brand{left:34px;top:48px;font-family:"Oswald",sans-serif;font-weight:600;color:var(--deep-blue);font-size:17px;line-height:19px;display:flex;align-items:center;gap:8px}
  .brand i{width:12px;height:12px;border-radius:50%;background:var(--deep-blue);display:inline-block}
  .services{left:34px;top:118px;list-style:none;font-family:"Oswald",sans-serif;font-weight:600;font-size:20px;line-height:27px;color:var(--brand-blue)}
  .services li::before{content:"";display:inline-block;width:9px;height:9px;border-radius:50%;background:var(--ink);margin-right:12px;vertical-align:4px}
  .offer-title{left:30px;top:404px;font-family:"Oswald",sans-serif;font-weight:600;font-size:22px;color:var(--brand-blue)}
  .offer-list{list-style:none;font-size:13.5px;line-height:16px}
  .offer-list li{position:relative;padding-left:20px;margin-bottom:12px}
  .offer-list--main{left:30px;top:446px;width:285px}
  .offer-list--extra{left:315px;top:446px;width:230px}
  .tick::before{content:"";position:absolute;left:3px;top:1px;width:5px;height:10px;border:solid var(--brand-blue);border-width:0 2.5px 2.5px 0;transform:rotate(40deg)}
  .dot::before{content:"";position:absolute;left:22px;top:5px;width:6px;height:6px;border-radius:50%;background:var(--brand-blue)}
  .offer-list--extra .dot{padding-left:38px}
</style>
</head>
<body>

<!-- FRONT -->
<section class="flyer flyer--front">
  <svg class="backdrop" viewBox="0 0 560 722" aria-hidden="false">
    <defs>
      <linearGradient id="fGrey" x1="0" y1="0" x2="0" y2="1">
        <stop offset="0" stop-color="#e9e9ea"/><stop offset=".5" stop-color="#f7f7f7"/><stop offset="1" stop-color="#cfd0d3"/>
      </linearGradient>
      <linearGradient id="fPhoto" x1="0" y1="0" x2="0" y2="1">
        <stop offset="0" stop-color="#dfe3e6"/><stop offset=".3" stop-color="#b9bcbd"/><stop offset=".62" stop-color="#5d5c5a"/><stop offset=".8" stop-color="#6f8250"/><stop offset="1" stop-color="#56713a"/>
      </linearGradient>
      <linearGradient id="fBlue" x1="0" y1="0" x2="1" y2="0">
        <stop offset="0" stop-color="#1b5aa9"/><stop offset="1" stop-color="#2a72c6"/>
      </linearGradient>
    </defs>
    <rect width="560" height="722" fill="url(#fGrey)"/>
    <!-- top swoosh -->
    <path d="M0 300 C120 400 250 455 420 420 C480 408 530 390 560 372 V400 C520 430 470 450 400 458 C250 480 110 440 0 390 Z" fill="var(--ink)"/>
    <path d="M0 300 C120 390 250 440 420 405 C480 393 530 375 560 357 V372 C530 390 480 408 420 420 C250 455 120 400 0 318 Z" fill="var(--white)"/>
    <path d="M0 300 V240 C110 345 240 395 400 370 C470 359 520 335 560 290 V357 C530 375 480 393 420 405 C250 440 120 390 0 300 Z" fill="url(#fBlue)"/>
    <g role="img" aria-label="Photo of a stone-clad house with a tall chimney and full-height glazed gable windows">
      <path d="M0 0 H560 V290 C520 335 470 359 400 370 C240 395 110 345 0 240 Z" fill="url(#fPhoto)"/>
    </g>
    <!-- logo oval -->
    <ellipse cx="450" cy="370" rx="88" ry="64" fill="var(--ink)"/>
    <ellipse cx="450" cy="370" rx="82" ry="58" fill="var(--white)"/>
    <ellipse cx="450" cy="370" rx="76" ry="52" fill="none" stroke="var(--brand-blue)" stroke-width="3"/>
    <!-- bottom swoosh -->
    <path d="M0 722 V690 C150 620 360 600 560 660 V722 Z" fill="var(--ink)"/>
    <path d="M0 722 V704 C160 636 370 620 560 676 V722 Z" fill="var(--white)"/>
    <path d="M0 722 V716 C170 650 380 636 560 690 V722 Z" fill="url(#fBlue)"/>
    <path d="M0 722 V716 C170 650 380 636 560 690 V722 Z" fill="url(#fBlue)" transform="translate(0,0)"/>
    <rect x="0" y="650" width="560" height="72" fill="url(#fBlue)" clip-path="inset(0)" opacity="0"/>
  </svg>
  <svg class="backdrop" viewBox="0 0 560 722" aria-hidden="true">
    <path d="M0 722 V712 C170 646 380 632 560 686 V722 Z" fill="var(--brand-blue)"/>
    <path d="M0 722 V708 C180 640 390 636 560 694 V722 Z" fill="var(--deep-blue)" opacity=".35"/>
  </svg>

  <div class="abs badge">DUNVARRA WINDOWS<br>&amp; HOME IMPROVEMENTS</div>

  <h1 class="abs headline headline--dark">DUNVARRA WINDOWS &amp; HOME IMPROVEMENTS</h1>
  <p class="abs headline headline--blue">is a family run business that offer full project management<br>from initial contact to final fitting</p>
  <p class="abs intro">Making sure all projects are finished to the highest standards and customers are fully satisfied</p>
  <div class="abs social" style="left:30px;top:614px">Like Us on <i></i><i></i></div>

  <p class="abs cta cta-label">Call Us for a free quote</p>
  <p class="abs cta cta-phone">087-5550142 / 085-5550193</p>
</section>

<!-- BACK -->
<section class="flyer flyer--back">
  <svg class="backdrop" viewBox="0 0 560 722">
    <defs>
      <linearGradient id="bGrey" x1="0" y1="0" x2="0" y2="1">
        <stop offset="0" stop-color="#ffffff"/><stop offset=".45" stop-color="#f3f3f3"/><stop offset=".75" stop-color="#e4e4e5"/><stop offset="1" stop-color="#cfd0d3"/>
      </linearGradient>
      <linearGradient id="bDoor" x1="0" y1="0" x2="1" y2="0">
        <stop offset="0" stop-color="#ffffff" stop-opacity="0"/><stop offset=".35" stop-color="#e6e7dc"/><stop offset=".55" stop-color="#8fb29d"/><stop offset=".85" stop-color="#86a994"/><stop offset="1" stop-color="#e8e6dc"/>
      </linearGradient>
      <linearGradient id="bBlue" x1="0" y1="0" x2="1" y2="0">
        <stop offset="0" stop-color="#1b5aa9"/><stop offset="1" stop-color="#2a72c6"/>
      </linearGradient>
    </defs>
    <rect width="560" height="722" fill="url(#bGrey)"/>
    <g role="img" aria-label="Photo of a sage green composite front door with leaded glass panels">
      <rect x="220" y="0" width="340" height="330" fill="url(#bDoor)"/>
    </g>
    <!-- top swoosh -->
    <path d="M0 240 C110 300 230 370 360 368 C450 366 510 330 560 300 V340 C500 380 440 398 360 398 C230 398 110 340 0 280 Z" fill="var(--ink)"/>
    <path d="M0 240 C110 296 230 358 360 356 C450 354 510 318 560 290 V300 C510 330 450 366 360 368 C230 370 110 300 0 252 Z" fill="var(--white)"/>
    <path d="M0 240 C110 296 230 358 360 356 C450 354 510 318 560 290 V238 C500 290 440 320 360 326 C230 334 110 280 0 236 Z" fill="url(#bBlue)"/>
    <!-- door circles -->
    <circle cx="104" cy="290" r="82" fill="var(--ink)"/>
    <circle cx="104" cy="290" r="76" fill="var(--white)"/>
    <g role="img" aria-label="Photo of a black composite front door with arched glass">
      <circle cx="104" cy="290" r="70" fill="#2a2d33"/>
    </g>
    <circle cx="275" cy="340" r="78" fill="var(--ink)"/>
    <circle cx="275" cy="340" r="72" fill="var(--white)"/>
    <circle cx="275" cy="340" r="68" fill="none" stroke="var(--brand-blue)" stroke-width="3"/>
    <g role="img" aria-label="Photo of a red composite front door with arched glass">
      <circle cx="275" cy="340" r="63" fill="#b4343a"/>
    </g>
    <!-- bottom swoosh -->
    <path d="M0 722 V650 C180 600 380 600 560 680 V722 Z" fill="var(--ink)"/>
    <path d="M0 722 V668 C190 616 390 624 560 698 V722 Z" fill="var(--white)"/>
    <path d="M0 722 V690 C190 634 390 634 560 704 V722 Z" fill="url(#bBlue)"/>
    <rect x="0" y="700" width="560" height="22" fill="url(#bBlue)"/>
  </svg>
  <svg class="backdrop" viewBox="0 0 560 722" aria-hidden="true">
    <path d="M0 722 V684 C190 630 390 632 560 702 V722 Z" fill="var(--brand-blue)"/>
  </svg>

  <div class="abs brand"><i></i><span>DUNVARRA WINDOWS<br>&amp; HOME IMPROVEMENTS</span></div>

  <ul class="abs services">
    <li>Construction Service &amp; Supply</li>
    <li>Home Window Service</li>
    <li>Home Decor</li>
  </ul>

  <h2 class="abs offer-title">What we offer</h2>
  <ul class="abs offer-list offer-list--main">
    <li class="tick">A rated windows double &amp; triple glazed</li>
    <li class="tick">All types of doors, patio ,French and UPVC</li>
    <li class="tick">Specialists in Verandel Composite doors</li>
    <li class="tick">Sunrooms &amp; Conservatories</li>
    <li class="tick">Emergency call out to replace broken glass to your secure home</li>
  </ul>
  <ul class="abs offer-list offer-list--extra">
    <li class="tick">All types of home improvements</li>
    <li class="dot">Extensions</li>
    <li class="dot">Renovations</li>
    <li class="dot">Roofing</li>
    <li class="dot">Fascia, soffit &amp; seamless gutters</li>
  </ul>

  <div class="abs social" style="left:432px;top:600px">Like Us on <i></i><i></i></div>

  <p class="abs cta cta-label">Call Us for a free quote</p>
  <p class="abs cta cta-phone">087-5550142 / 085-5550193</p>
</section>

</body>
</html>
```